magcian / mentalist needs flyer desined to send potentisl clients

I need a design that's contemporary, sharp, fun, and professional that will get the attention of whoever receives the flyer very quickly. This is for a tri-fold flyer design.

I've been performing magic for over 40 years. I've performed close-up,
parlor, and stage shows. I've been an Master of Ceremonies, Key Note
Speaker (using magic during presentations to help build on a point or
topic, while keeping the audience entertained and educated on the topic or
topics the client has asked me to focus). I've worked trade shows and
sales training incorporating magic as well. I did private shows in Las
Vegas and L.A. back in the late 90's as well.

I do have website / wesleytorvandmagic.example for your to check out.

Target Market(s)

The target audience is corporation Event Planners, Marketing and Sales
managers, casino & hotel entertainment directors, as well as private
businesses looking for unique entertainment options.

Industry/Entity Type

Entertainment Industry

Logo Text

Here are a couple of ideas: your mind is my playground, neural entertainer, professor of mysteries, master of your mind

Requirements
Must have
• I like the black and white look (I think it looks nice, but open to other
• ideas and creativity. Being I'm a magician and mentalist, I'd like for
• both venues to be conveyed somehow. My magic is clean and corporate and family friendly.
Nice to have
• I do have website / wesleytorvandmagic.example for your to check out.
• My current business card is attached for review. I'll also attach photos
• I'd like to share, but was unable when I last attempted do sign up. Some
• of the files were too big and I'm not savvy enough to make them smaller,
• but think there might be some potential with a couple.
Should not have
• cartoons or cartoonish graphics. no rabbits, doves, magicians, wands, or top hats.

```html
<!DOCTYPE html>
<html lang="en">
<head>
<meta charset="utf-8">
<title>Wesley Torvand – Tri-fold Flyer</title>
<link href="https://fonts.googleapis.com/css2?family=Source+Sans+3:wght@400;600&family=Caveat:wght@400;600&display=swap" rel="stylesheet">
<style>
  :root{
    --canvas:#d7d7d7;
    --ink:#ffffff;
    --ink-soft:#e6e6e6;
    --panel-black:#0b0b0b;
    --panel-dark:#161616;
    --shadow:rgba(0,0,0,.45);
    --sans:"Source Sans 3", Arial, sans-serif;
    --script:"Caveat", cursive;
  }
  *{box-sizing:border-box;margin:0;padding:0}
  html,body{width:818px;height:1200px;overflow:hidden}
  body{background:var(--canvas);font-family:var(--sans);color:var(--ink);position:relative}

  .spread{position:absolute;left:39px;width:740px;height:560px;background:var(--panel-black);box-shadow:4px 5px 8px var(--shadow);overflow:hidden}
  .spread--outside{top:24px}
  .spread--inside{top:616px}
  .spread__art{position:absolute;inset:0;display:block}

  .block{position:absolute}
  .heading{font-weight:600;font-size:12.5px;letter-spacing:.1px;margin-bottom:6px}
  .heading--large{font-weight:400;font-size:18px;margin-bottom:10px}
  .body-copy{font-size:8.6px;line-height:12px;text-align:justify;color:var(--ink-soft)}
  .body-copy p+p{margin-top:12px}
  .body-copy strong{font-weight:600;color:var(--ink)}

  .about{left:16px;top:36px;width:211px}

  .quote{left:268px;top:172px;width:190px;font-family:var(--script);font-size:21px;line-height:27px;color:#d9d9d9;font-style:italic}
  .quote__mark{font-family:Georgia,serif;font-size:26px;color:#8c8c8c;font-style:normal;line-height:0}

  .masthead{left:486px;top:30px;width:254px;text-align:center}
  .masthead__name{font-family:var(--script);font-weight:600;font-size:34px;line-height:38px;letter-spacing:1px}
  .masthead__tagline{font-size:12px;margin-top:8px;letter-spacing:.2px}

  .contact{left:262px;top:470px;width:200px;text-align:center}
  .contact__name{font-size:17px;font-weight:400}
  .contact__tagline{font-size:5.6px;font-weight:600;margin-top:5px;letter-spacing:.2px}
  .contact__phone{font-size:9.5px;font-weight:600;margin-top:6px;display:flex;justify-content:center;align-items:center;gap:4px}
  .contact__web{font-size:6.5px;margin-top:6px}
  .site-url{left:520px;top:528px;width:180px;text-align:center;font-size:8.5px;font-weight:600}

  .services{left:16px;top:22px;width:220px}
  .services__intro{font-size:9.4px;line-height:12.5px}
  .services__list{list-style:none;margin-top:10px}
  .services__list li{font-size:10.5px;line-height:18px;display:flex;align-items:center;gap:7px}
  .services__list li::before{content:"";width:6px;height:6px;border-radius:50%;background:#cfcfcf;box-shadow:inset 0 0 0 1.5px #555}
  .keynote{left:263px;top:170px;width:212px}
  .corporate{left:18px;top:442px;width:216px}
  .shows{left:506px;top:490px;width:222px}
  .shows .body-copy,.corporate .body-copy{text-align:left}
</style>
</head>
<body>

<section class="spread spread--outside" aria-label="Outside of tri-fold">
  <svg class="spread__art" viewBox="0 0 740 560">
    <defs>
      <linearGradient id="upperShade" x1="0" y1="0" x2="1" y2="0">
        <stop offset="0" stop-color="#202020"/><stop offset=".5" stop-color="#2a2a2a"/><stop offset="1" stop-color="#0f0f0f"/>
      </linearGradient>
      <linearGradient id="lowerShade" x1="0" y1="0" x2="0" y2="1">
        <stop offset="0" stop-color="#4a4a4a"/><stop offset="1" stop-color="#242424"/>
      </linearGradient>
      <linearGradient id="photoMono" x1="0" y1="0" x2="1" y2="1">
        <stop offset="0" stop-color="#3a3a3a"/><stop offset=".45" stop-color="#8e8e8e"/><stop offset="1" stop-color="#262626"/>
      </linearGradient>
      <linearGradient id="photoWarm" x1="0" y1="0" x2="1" y2="1">
        <stop offset="0" stop-color="#2a2018"/><stop offset=".5" stop-color="#5a4634"/><stop offset="1" stop-color="#15100c"/>
      </linearGradient>
      <linearGradient id="portrait" x1="0" y1="0" x2="0" y2="1">
        <stop offset="0" stop-color="#c3ccd4"/><stop offset="1" stop-color="#7a8794"/>
      </linearGradient>
    </defs>
    <rect width="740" height="560" fill="#111"/>
    <rect width="241" height="560" fill="var(--panel-black)"/>
    <rect x="241" width="499" height="560" fill="url(#upperShade)"/>
    <rect x="486" y="168" width="254" height="300" fill="url(#photoMono)" role="img" aria-label="Black and white photo of the magician performing a rope trick with a guest"/>
    <path d="M241,128 C360,85 470,125 560,155 C640,180 700,192 740,190" fill="none" stroke="#8a8a8a" stroke-width="16" opacity=".55"/>
    <path d="M241,120 C360,78 470,118 560,148 C640,172 700,184 740,182" fill="none" stroke="#fff" stroke-width="5"/>
    <path d="M0,395 C90,365 200,368 300,405 C400,442 590,490 740,470 L740,560 L0,560Z" fill="url(#lowerShade)"/>
    <path d="M0,400 C60,380 160,372 241,385 L241,560 L0,560Z" fill="url(#photoWarm)" role="img" aria-label="Stage photo of the magician with a microphone and a volunteer"/>
    <path d="M0,388 C90,358 200,361 300,398 C400,435 590,483 740,463" fill="none" stroke="#9a9a9a" stroke-width="16" opacity=".6"/>
    <path d="M0,381 C90,351 200,354 300,391 C400,428 590,476 740,456" fill="none" stroke="#fff" stroke-width="4"/>
    <circle cx="362" cy="382" r="61" fill="#d8d8d8"/>
    <circle cx="362" cy="382" r="55" fill="url(#portrait)" role="img" aria-label="Portrait photo of Wesley Torvand"/>
  </svg>

  <div class="block about">
    <h2 class="heading heading--large">About Wesley</h2>
    <div class="body-copy">
      <p>From sleight-of-hand close-up magic with small objects like cards, coins, and dollar bills, mentalism, to stage illusions that can be seen by hundreds of people at a time, your guests will experience magic exquisitely performed by a master of his craft.</p>
      <p><strong>I’m a professional entertainer.</strong><br>I’ve been performing magic for over 40 years. I’ve been an Master of Ceremonies, Key Note Speaker (using magic during presentations to help build on a point or topic, while keeping the audience entertained and educated on the topic or topics the client has asked me to focus). I’ve performed all over the country for major corporations which means you’re getting tried and true, first-rate entertainment.</p>
      <p><strong>My performances are guaranteed!</strong><br>I pride myself on building relationships with my customers, so I’m not happy unless you’re happy. I guarantee your guests will have a great time and will thank you for having me there.</p>
    </div>
  </div>

  <blockquote class="block quote"><span class="quote__mark">“</span>If magic really existed, this is what it would look like<span class="quote__mark">”</span></blockquote>

  <div class="block masthead">
    <h1 class="masthead__name">Wesley Torvand</h1>
    <p class="masthead__tagline">MAGICIAN • MENTALIST • ENTERTAINER</p>
  </div>

  <div class="block contact">
    <p class="contact__name">Wesley Torvand</p>
    <p class="contact__tagline">MAGICIAN • MENTALIST • ENTERTAINER</p>
    <p class="contact__phone">
      <svg width="9" height="9" viewBox="0 0 24 24" aria-hidden="true"><circle cx="12" cy="12" r="10.5" fill="none" stroke="#fff" stroke-width="2"/><path d="M8 6.5l2 2-1.2 1.6c.8 1.8 2.3 3.3 4.1 4.1l1.6-1.2 2 2-1.6 2c-4.4-.4-8.5-4.5-8.9-8.9z" fill="#fff"/></svg>
      505 555 0142
    </p>
    <p class="contact__web">www.wesleytorvandmagic.example</p>
  </div>

  <p class="block site-url">www.wesleytorvandmagic.example</p>
</section>

<section class="spread spread--inside" aria-label="Inside of tri-fold">
  <svg class="spread__art" viewBox="0 0 740 560">
    <defs>
      <linearGradient id="leftShade" x1="0" y1="0" x2="1" y2="0">
        <stop offset="0" stop-color="#222"/><stop offset="1" stop-color="#111"/>
      </linearGradient>
      <linearGradient id="baseShade" x1="0" y1="0" x2="0" y2="1">
        <stop offset="0" stop-color="#474747"/><stop offset="1" stop-color="#262626"/>
      </linearGradient>
      <linearGradient id="photoEvent" x1="0" y1="0" x2="1" y2="1">
        <stop offset="0" stop-color="#3b2a1c"/><stop offset=".5" stop-color="#7a5b40"/><stop offset="1" stop-color="#1c140e"/>
      </linearGradient>
      <linearGradient id="photoStage" x1="0" y1="0" x2="0" y2="1">
        <stop offset="0" stop-color="#3a1e10"/><stop offset=".55" stop-color="#6b4a35"/><stop offset="1" stop-color="#2a1a12"/>
      </linearGradient>
    </defs>
    <rect width="740" height="560" fill="#0b0b0b"/>
    <rect width="247" height="560" fill="url(#leftShade)"/>
    <path d="M247,0 H490 V135 C420,108 330,95 247,115Z" fill="url(#photoEvent)" role="img" aria-label="Photo of a close-up trick at a banquet table"/>
    <rect x="0" y="150" width="247" height="250" fill="url(#photoEvent)" role="img" aria-label="Photo of the magician performing a rope trick with a volunteer holding scissors"/>
    <path d="M0,0 H247 V115 C170,140 80,190 0,212Z" fill="url(#leftShade)"/>
    <path d="M0,219 C80,197 170,147 247,122 C330,102 420,115 490,142" fill="none" stroke="#9a9a9a" stroke-width="16" opacity=".6"/>
    <path d="M0,212 C80,190 170,140 247,115 C330,95 420,108 490,135" fill="none" stroke="#fff" stroke-width="4"/>
    <rect x="490" y="0" width="250" height="470" fill="url(#photoStage)" role="img" aria-label="Stage photo of the magician performing with a smiling guest"/>
    <path d="M490,392 C570,417 650,457 740,472 V560 H490Z" fill="#121212"/>
    <path d="M490,390 C570,415 650,455 740,470" fill="none" stroke="#8f8f8f" stroke-width="16" opacity=".6"/>
    <path d="M490,384 C570,409 650,449 740,464" fill="none" stroke="#fff" stroke-width="4"/>
    <path d="M0,425 C90,380 230,365 330,380 C410,392 460,405 490,412 V560 H0Z" fill="url(#baseShade)"/>
    <rect x="247" y="392" width="243" height="168" fill="url(#photoEvent)" role="img" aria-label="Photo of a mentalism routine with a blindfolded volunteer"/>
    <path d="M0,426 C90,381 230,366 330,381 C410,393 460,406 490,413" fill="none" stroke="#9a9a9a" stroke-width="16" opacity=".6"/>
    <path d="M0,419 C90,374 230,359 330,374 C410,386 460,399 490,406" fill="none" stroke="#fff" stroke-width="4"/>
  </svg>

  <div class="block services">
    <h2 class="heading">Wesley Services</h2>
    <p class="body-copy services__intro">Wesley entertains and presents key content with magic, humor and audience participation so that you learn while you laugh!</p>
    <ul class="services__list">
      <li>Corporate Magic</li>
      <li>Healing with Magic</li>
      <li>Keynote Speaker</li>
      <li>Magic Shows</li>
    </ul>
  </div>

  <div class="block keynote">
    <h2 class="heading">Keynote Speaker</h2>
    <div class="body-copy">
      <p>Your audience will be captivated with Wesley’s engaging &amp; informative insights on many topics mastered with over 30 years in sales, sales training, and sales management using his “Magic Formula” to personalize his presentation to fit your needs.</p>
      <p>Wesley presents key content with magic, humor &amp; audience participation so that you “learn while you laugh”!</p>
    </div>
  </div>

  <div class="block corporate">
    <h2 class="heading">Corporate Magic</h2>
    <p class="body-copy">Magic at your corporate function adds an element that will distinguish your company from others. Having a close up entertainer at your events brings the entertainment and amazement of watching an illusionist into a smaller venue, allowing the feeling of an intimate show for you and your guests to enjoy and create memories together.</p>
  </div>

  <div class="block shows">
    <h2 class="heading">Magic Shows</h2>
    <p class="body-copy">From close up, parlor, to company picnics to black tie affairs, to private shows or large public venues, Wesley can build a show to fit your needs.</p>
  </div>
</section>

</body>
</html>
```